vantro - business cards

Need business card designs - logo provided - see www.vantro.co.nz

Industry/Entity Type

Business

Requirements
Must have
• logo - provided in attachments
• www.vantro.co.nz

```html
<!DOCTYPE html>
<html lang="en">
<head>
<meta charset="utf-8">
<title>vantro business cards</title>
<link href="https://fonts.googleapis.com/css2?family=Tinos:wght@400;700&display=swap" rel="stylesheet">
<style>
  :root {
    --bg-light: #f2f2f2;
    --bg-dark: #b9b9b9;
    --card-white: #fafafa;
    --charcoal: #333333;
    --charcoal-soft: #555555;
    --orange: #f07a22;
    --orange-soft: #f6a566;
    --text-light: #e8e8e8;
    --ink: #3a3a3a;
  }
  * { margin: 0; padding: 0; box-sizing: border-box; }
  html, body { width: 1200px; height: 787px; overflow: hidden; }
  body {
    background: radial-gradient(ellipse at 50% 40%, var(--bg-light) 0%, var(--bg-dark) 100%);
    font-family: "Tinos", "Times New Roman", serif;
    position: relative;
  }
  .card {
    position: absolute;
    top: 238px;
    width: 540px;
    height: 310px;
    background: var(--card-white);
    overflow: hidden;
    box-shadow: 0 6px 18px rgba(0,0,0,0.25);
  }
  .card--front { left: 40px; }
  .card--back { left: 620px; }

  /* front */
  .disc { position: absolute; border-radius: 50%; }
  .disc--shadow { width: 400px; height: 400px; left: 16px; top: -30px; background: var(--charcoal-soft); }
  .disc--main { width: 400px; height: 400px; left: 30px; top: -45px; background: var(--charcoal); }
  .disc--accent-ring { width: 250px; height: 250px; left: 385px; top: 230px; background: var(--orange-soft); }
  .disc--accent { width: 250px; height: 250px; left: 400px; top: 245px; background: var(--orange); }

  .brand {
    position: absolute;
    display: flex;
    align-items: center;
    gap: 7px;
    font-size: 22px;
    font-weight: 700;
    color: var(--ink);
  }
  .brand__dot { width: 14px; height: 14px; border-radius: 50%; background: var(--orange); }
  .card--front .brand { right: 22px; top: 22px; }

  .details { position: absolute; left: 120px; top: 42px; color: var(--text-light); }
  .details__name { font-size: 30px; letter-spacing: 1px; line-height: 1; margin-left: 18px; }
  .details__title { font-size: 15px; color: var(--orange); margin-left: 165px; margin-top: 4px; }
  .details__contact { font-size: 12px; line-height: 1.35; margin: 24px 0 0 10px; letter-spacing: 0.3px; }
  .details__rule { width: 258px; height: 1.5px; background: var(--orange); margin: 22px 0 10px 0; }
  .details__company { font-size: 15px; color: var(--orange); letter-spacing: 0.5px; }
  .details__lines { font-size: 11.5px; line-height: 1.3; letter-spacing: 0.2px; margin-left: -4px; }

  /* back */
  .band { position: absolute; left: 0; width: 100%; }
  .band--top { top: 0; height: 120px; background: var(--charcoal-soft); }
  .band--bottom { bottom: 0; height: 85px; background: var(--orange); }
  .card--back .brand { right: 30px; top: 150px; font-size: 34px; gap: 10px; }
  .card--back .brand__dot { width: 20px; height: 20px; }
</style>
</head>
<body>
  <section class="card card--front" aria-label="Business card front">
    <div class="disc disc--shadow"></div>
    <div class="disc disc--main"></div>
    <div class="disc disc--accent-ring"></div>
    <div class="disc disc--accent"></div>

    <div class="brand"><span class="brand__dot"></span><span>vantro</span></div>

    <div class="details">
      <p class="details__name">LIAM CARTER</p>
      <p class="details__title">TITLE HERE</p>
      <p class="details__contact">PHONE : +64 00 000 00000<br>EMAIL : VANTRO@GMAIL.COM</p>
      <div class="details__rule"></div>
      <p class="details__company">"VANTRO"</p>
      <p class="details__lines">
        COMPANY PHONE NUMBER : 0800 2 VANTRO<br>
        (0800 82 68 76)<br>
        POSTAL ADDRESS (3 LINES, OR IN-LINE)<br>
        WEB ADDRESS (WWW.VANTRO.CO.NZ)
      </p>
    </div>
  </section>

  <section class="card card--back" aria-label="Business card back">
    <div class="band band--top"></div>
    <div class="brand"><span class="brand__dot"></span><span>vantro</span></div>
    <div class="band band--bottom"></div>
  </section>
</body>
</html>
```